Shopify Design for Back Pain Patch

We need a design for the Shopify-based homepage of the new Vortilo Spine Patch.

The Vortilo spine patch absorbs the surface energy produced by your body when you are in pain and redistributes it, reducing your discomfort. It is approximately 5” x 5” in size, with an adhesive backing on one side and a cloth-like exterior that is neutral/light tan in color.

We need a website design that matches our packaging (see attached assets). This includes the blue/orange color scheme and our key messages:

-Natural relief for back pain
-Soothes using your body's natural energy
-Odorless, Gentle, Easy to Use
-Reusable up to 5 days

We are going to be using the Shopify platform for this website, so we'd like the design to be usable with this theme:
http://pliantframe.examplestore.net/pages/theme-features

We will do all of the coding, but please keep this layout in mind for the design.

Target Market(s)

The Vortilo Spine Patch is targeted to people suffering from mild to moderate, chronic back pain, but who desire to continue leading active lives.

Industry/Entity Type

Adhesive

Requirements
Must have
• The design needs to have the same look and feel as the packaging for the back patch. Please feel free to use any of the attached assets in your design (doesn't need to be all).
Should not have
• We do not want to see stock photography other than the assets provided.

```html
<!DOCTYPE html>
<html lang="en">
<head>
<meta charset="utf-8">
<title>Vortilo Spine Patch</title>
<link rel="stylesheet" href="https://fonts.googleapis.com/css2?family=Rokkitt:wght@300;400&family=Open+Sans:wght@600&display=swap">
<style>
:root{
  --blue:#1f74b8;
  --orange:#f2841f;
  --header-bg:#fafbfc;
  --footer-bg:#ececec;
  --panel:rgba(255,255,255,.7);
  --rule:#b9c6d1;
  --sky-deep:#5f93c4;
  --sky-light:#c9dcec;
  --glow:#f4f8fb;
  --steel:#6f7d8a;
  --shadow:#2c323b;
}
*{margin:0;padding:0;box-sizing:border-box}
html,body{width:1200px;height:858px;overflow:hidden;background:#fff}
body{font-family:"Rokkitt",serif;color:var(--blue);position:relative}
a{color:inherit;text-decoration:none}

.site-header{position:absolute;left:0;top:0;width:1200px;height:125px;background:var(--header-bg)}
.brand{position:absolute;left:157px;top:40px;display:flex;align-items:center;gap:8px}
.brand-dot{width:14px;height:14px;border-radius:50%;background:var(--orange)}
.brand-name{font-family:"Open Sans",sans-serif;font-weight:600;font-size:26px;color:var(--orange);letter-spacing:-.3px}

.utility{position:absolute;top:22px;left:715px;display:flex;align-items:center;gap:16px;font-size:16px}
.utility a{display:flex;align-items:center;gap:4px}
.utility svg{fill:var(--blue)}
.login{position:absolute;left:912px;top:15px;width:153px;height:30px;background:var(--blue);color:#fff;display:flex;align-items:center;gap:12px;padding-left:14px;font-size:16px}
.login svg{fill:#fff}

.main-nav{position:absolute;top:73px;left:390px;width:678px;display:flex;justify-content:space-between;font-size:17px;font-weight:300;letter-spacing:.3px}
.main-nav .current{color:var(--orange)}

.hero{position:absolute;left:0;top:125px;width:1200px;height:651px;overflow:hidden}
.hero-photo{position:absolute;inset:0;
  background:
    radial-gradient(ellipse 380px 300px at 640px 90px, var(--glow) 0%, rgba(244,248,251,.6) 45%, rgba(244,248,251,0) 100%),
    radial-gradient(ellipse 520px 420px at 930px 470px, rgba(44,50,59,.75) 0%, rgba(44,50,59,.35) 55%, rgba(44,50,59,0) 100%),
    linear-gradient(180deg, rgba(44,50,59,0) 55%, rgba(44,50,59,.55) 100%),
    linear-gradient(100deg, var(--sky-deep) 0%, var(--sky-light) 45%, #b7c8d6 70%, var(--steel) 100%)}

.benefits{position:absolute;left:157px;top:186px;width:443px;height:275px;background:var(--panel);padding:30px 18px 0 37px}
.benefits li{list-style:none;display:flex;align-items:flex-start;gap:16px;font-size:26px;line-height:28px;padding:10px 0 11px;border-bottom:2px dotted var(--rule)}
.benefits li:last-child{border-bottom:none}
.benefits svg{flex:none;margin-top:4px}

.site-footer{position:absolute;left:0;top:776px;width:1200px;height:82px;background:var(--footer-bg)}
.footer-nav{position:absolute;left:156px;top:36px;display:flex;gap:17px;font-size:13px}
.social{position:absolute;left:862px;top:0;display:flex;gap:16px}
.social-item{display:flex;flex-direction:column;align-items:center}
.social-item .chain{width:1px;height:22px;background:#b8b8b8}
.social-item .badge{width:30px;height:30px;border-radius:50%}
.s1{background:#c74f9c}.s2{background:#58b4e0}.s3{background:#5b78b3}.s4{background:#f08a3a}
.social-item:nth-child(2) .chain,.social-item:nth-child(3) .chain{height:32px}
</style>
</head>
<body>
<header class="site-header">
  <a class="brand" href="#"><span class="brand-dot"></span><span class="brand-name">Vortilo Spine Patch</span></a>
  <nav class="utility">
    <a href="#">Home <svg width="16" height="14" viewBox="0 0 16 14"><path d="M8 0 16 7H13V14H10V9H6V14H3V7H0Z"/></svg></a>
    <a href="#">Mail <svg width="18" height="12" viewBox="0 0 18 12"><path d="M0 0H18V12H0ZM1.5 1.5 9 7 16.5 1.5Z" fill-rule="evenodd"/></svg></a>
    <a href="#">Cart <svg width="18" height="14" viewBox="0 0 18 14"><path d="M0 0H3L4 2H18L16 9H5ZM5 11a1.5 1.5 0 1 0 .01 0ZM14 11a1.5 1.5 0 1 0 .01 0Z"/></svg></a>
  </nav>
  <a class="login" href="#"><svg width="13" height="17" viewBox="0 0 13 17"><path d="M3 7V4.5a3.5 3.5 0 0 1 7 0V7H8.5V4.5a2 2 0 0 0-4 0V7ZM0 7H13V17H0Z"/></svg>Customer login</a>
  <nav class="main-nav">
    <a class="current" href="#">HOME</a><span>|</span>
    <a href="#">ABOUT US</a><span>|</span>
    <a href="#">OUR BLOG</a><span>|</span>
    <a href="#">OUR PRODUCT</a><span>|</span>
    <a href="#">BUY NOW</a><span>|</span>
    <a href="#">CONTACT&nbsp; US</a>
  </nav>
</header>

<section class="hero">
  <div class="hero-photo" role="img" aria-label="Photo of a smiling cyclist in a red, white and black jersey seated by a riverside railing beside his road bike, a tan spine patch on his lower back, bright sky and city buildings behind"></div>
  <ul class="benefits">
    <li><svg width="40" height="22" viewBox="0 0 40 22"><path d="M0 9H28V2L40 11 28 20V13H0Z" fill="#f2841f"/></svg>Natural relief for back pain</li>
    <li><svg width="40" height="22" viewBox="0 0 40 22"><path d="M0 9H28V2L40 11 28 20V13H0Z" fill="#f2841f"/></svg>Soothes using your body's natural energy</li>
    <li><svg width="40" height="22" viewBox="0 0 40 22"><path d="M0 9H28V2L40 11 28 20V13H0Z" fill="#f2841f"/></svg>Odorless, Gentle, Easy to Use</li>
    <li><svg width="40" height="22" viewBox="0 0 40 22"><path d="M0 9H28V2L40 11 28 20V13H0Z" fill="#f2841f"/></svg>Reusable up to 5 days</li>
  </ul>
</section>

<footer class="site-footer">
  <nav class="footer-nav">
    <a href="#">HOME</a><span>|</span>
    <a href="#">ABOUT US</a><span>|</span>
    <a href="#">OUR BLOG</a><span>|</span>
    <a href="#">OUR PRODUCT</a><span>|</span>
    <a href="#">BUY NOW</a><span>|</span>
    <a href="#">CONTACT&nbsp; US</a>
  </nav>
  <div class="social">
    <a class="social-item" href="#" aria-label="Social link"><span class="chain"></span><span class="badge s1"></span></a>
    <a class="social-item" href="#" aria-label="Social link"><span class="chain"></span><span class="badge s2"></span></a>
    <a class="social-item" href="#" aria-label="Social link"><span class="chain"></span><span class="badge s3"></span></a>
    <a class="social-item" href="#" aria-label="Social link"><span class="chain"></span><span class="badge s4"></span></a>
  </div>
</footer>
</body>
</html>
```